Business Card & Logo Design - Hedge Fund

We need a business card and logo design for a hedge fund. The hedge fund is named Morvane Equity LLC. Morvane Equity was created by finance professors and the strategy is based academic research that looks for patterns in stock prices. The design should look conservative, solid, strong. We favor a classic style - nothing flashy. The logo can relate to the name Morvane Equity, or it could involve a symbol design that connotes "science" . We are open to ideas. We do not want alot of colors - but if any, color - blue is preferred. The font that seems to look best for the name (Morvane Equity) is arial black. We are open to ideas. Most important - we want to see a mock up of an actual business card with the logo concept embedded. The business card should include space for : company name, individual name, position title, cell phone, address. We hope to have this work done by Sept. 8.

Target Market(s)

We will be meeting with and giving the business card to institutions and high net worth individuals.

Industry/Entity Type

Investment Advisory

Contact Information for Business Card

Company name - Morvane Equity LLC
Individual name - Peter Dalby
Title - Portfolio Manager
Cell - (412) 555-0187
Address - 2650 Birchmont Lane, Suite 300, Atlanta GA 30327

Font styles to use
Other font styles liked:
• Arial

Colors
3277b5
0255a3
85acd3
cedeed
fdf9cf
d9d9d9
e6e6e6
f04a50
6b449b

Requirements
Must have
• Must have card details that are sited above.
• We would like a logo related to the name (Morvane Equity) or concept of the fund.
Nice to have
• We want conservative / understated / clean crisp look.
• If any colors - we prefer conservative appearance - blue / gray.
• I have enclosed an example of a card style that looks attractive - please do not exactly copy this card. This is not our company or logo. I feel the layout is attractive - just as an example
Should not have
• Avoid too much color.
• I have selected some preferred colors. Please do not use all of the colors - I have selected a few that might work - but I am not sure. We are open to your ideas so please do not feel the need to use all or any of these.

```html
<!DOCTYPE html>
<html lang="en">
<head>
<meta charset="utf-8">
<title>Morvane Equity LLC – Business Card</title>
<link rel="stylesheet" href="https://fonts.googleapis.com/css2?family=Arimo:wght@400;700&display=swap">
<style>
  :root {
    --stage: #e6e6e6;
    --card-white: #ffffff;
    --brand-blue: #0a4fd6;
    --brand-blue-deep: #0b3fc8;
    --brand-blue-light: #3aa0f0;
    --name-blue: #2b9be8;
    --text-gray: #5a5f66;
    --rule-gray: #9aa0a6;
    --white: #ffffff;
  }
  * { box-sizing: border-box; margin: 0; padding: 0; }
  html, body {
    width: 1200px; height: 1200px; overflow: hidden;
    background: var(--stage);
    font-family: "Arimo", Arial, sans-serif;
  }
  .stage {
    width: 1200px; height: 1200px;
    display: flex; flex-direction: column;
    align-items: center; justify-content: center; gap: 60px;
  }
  .card {
    width: 900px; height: 514px;
    position: relative; overflow: hidden;
    box-shadow: 0 6px 18px rgba(0,0,0,0.12);
  }

  /* Front (contact side) */
  .card--front {
    background: var(--card-white);
    display: flex; align-items: center;
  }
  .front__brand {
    width: 390px;
    display: flex; align-items: center; justify-content: center; gap: 14px;
  }
  .brand-dot {
    width: 22px; height: 22px; border-radius: 50%;
    background: var(--brand-blue);
  }
  .brand-name {
    font-weight: 700; font-size: 34px; color: var(--brand-blue);
    letter-spacing: -0.5px;
  }
  .front__rule {
    width: 2px; height: 250px; background: var(--rule-gray); opacity: 0.7;
  }
  .front__details { padding-left: 44px; }
  .person-name {
    font-weight: 700; font-size: 40px; color: var(--name-blue);
    margin-bottom: 6px;
  }
  .person-title {
    font-size: 30px; color: var(--text-gray); margin-bottom: 30px;
  }
  .contact-line {
    font-size: 27px; color: var(--text-gray); line-height: 1.32;
  }

  /* Back (company side) */
  .card--back {
    background: radial-gradient(ellipse at 52% 42%, #3fb0f7 0%, #1f7ff0 30%, var(--brand-blue) 62%, var(--brand-blue-deep) 100%);
    display: flex; flex-direction: column; align-items: center; justify-content: center;
  }
  .back__brand {
    display: flex; align-items: center; gap: 22px; margin-bottom: 70px;
  }
  .back__brand .brand-dot { width: 40px; height: 40px; background: var(--white); }
  .back__brand .brand-name { font-size: 64px; color: var(--white); }
  .company-line {
    font-size: 40px; color: var(--white); letter-spacing: 0.5px;
    text-transform: uppercase;
  }
</style>
</head>
<body>
<main class="stage">
  <section class="card card--front" aria-label="Business card front">
    <div class="front__brand">
      <span class="brand-dot"></span>
      <span class="brand-name">Morvane Equity</span>
    </div>
    <div class="front__rule"></div>
    <div class="front__details">
      <p class="person-name">Peter Dalby</p>
      <p class="person-title">Portfolio Manager</p>
      <p class="contact-line">Cell - (412) 555-0187</p>
      <p class="contact-line">2650 Birchmont Lane,</p>
      <p class="contact-line">Suite 300, Atlanta GA 30327</p>
    </div>
  </section>

  <section class="card card--back" aria-label="Business card back">
    <div class="back__brand">
      <span class="brand-dot"></span>
      <span class="brand-name">Morvane Equity</span>
    </div>
    <p class="company-line">Morvane Equity LLC</p>
  </section>
</main>
</body>
</html>
```